Event Graphic for Free Community Event

We need a graphic created for a community event that is aimed at families with younger children called Tots Jamboree. This is a free event and has a fair/carnival feel to it with rides, games, and food. I need the graphic to be flexible enough to be able to be modified and used in a variety of ways on different print and digital marketing materials. I also need the centerpiece of the design to be an event logo that can be used as a standalone element.

The overall feel needs to be fun and friendly with a slightly modern edge to it. Attached are some images used in past events. These are for reference only and do not need to be simulated or used in the final product.

Target Market(s)

Families with children

Industry/Entity Type

Church

Font styles to use
Sans Serif

Requirements
Must have
• - Logo that incorporates the event name
- Event Date: September 19 2020
- Event Time: 10am - 2pm
- Church name and logo incorporated: Bright Harbor Community Church (see attached logo files)
Nice to have
• - Bright colors
- Flexible design elements that are interchangeable and scalable for use of the design in different layouts across different mediums and materials.
Should not have
• - Any references or images related to drugs, alcohol, tobacco, or other subjects that would be inappropriate for children.

```html
<!DOCTYPE html>
<html lang="en">
<head>
<meta charset="utf-8">
<title>Tots Jamboree – Bright Harbor Community Church</title>
<link rel="stylesheet" href="https://fonts.googleapis.com/css2?family=Chewy&family=Oswald:wght@500&display=swap">
<style>
  :root {
    --paint-orange: #ffb000;
    --paint-yellow: #ffe800;
    --paint-red: #ff1500;
    --paint-pink: #ff1a78;
    --paint-magenta: #e0168f;
    --ink: #231f20;
    --headline-white: #ffffff;
    --headline-yellow: #fff200;
    --headline-shadow: #8a0010;
  }
  html, body {
    margin: 0;
    padding: 0;
    overflow: hidden;
    background: #ffffff;
  }
  .event-graphic {
    position: relative;
    width: 1200px;
    height: 675px;
    overflow: hidden;
  }
  .paint-splash-background {
    position: absolute;
    inset: 0;
    background: linear-gradient(100deg,
      var(--paint-orange) 0%,
      var(--paint-yellow) 30%,
      var(--paint-yellow) 44%,
      var(--paint-red) 60%,
      var(--paint-red) 72%,
      var(--paint-pink) 88%,
      var(--paint-magenta) 100%);
  }
  .church-identity {
    position: absolute;
    left: 190px;
    top: 214px;
    width: 290px;
    display: flex;
    flex-direction: column;
    align-items: center;
  }
  .church-identity__dot {
    width: 204px;
    height: 204px;
    border-radius: 50%;
    background: var(--ink);
  }
  .church-identity__name {
    margin-top: 18px;
    font-family: "Oswald", sans-serif;
    font-weight: 500;
    font-size: 22px;
    line-height: 1;
    letter-spacing: -0.3px;
    text-transform: uppercase;
    color: var(--ink);
    white-space: nowrap;
  }
  .event-logo {
    position: absolute;
    left: 722px;
    top: 128px;
    width: 280px;
    transform: rotate(-6deg);
    transform-origin: left top;
    font-family: "Chewy", sans-serif;
    text-shadow: 2px 3px 0 var(--headline-shadow);
  }
  .event-logo__free {
    display: block;
    font-size: 72px;
    line-height: 0.9;
    color: var(--headline-yellow);
  }
  .event-logo__name {
    display: block;
    color: var(--headline-white);
    line-height: 0.88;
  }
  .event-logo__name-top {
    display: block;
    font-size: 118px;
  }
  .event-logo__name-bottom {
    display: block;
    font-size: 64px;
  }
  .event-logo__details {
    display: block;
    margin-top: 14px;
    padding-left: 12px;
    font-size: 38px;
    line-height: 1.1;
    color: var(--headline-white);
  }
</style>
</head>
<body>
  <main class="event-graphic">
    <div class="paint-splash-background" role="img" aria-label="Bright paint splashes in orange, yellow, red and pink"></div>

    <section class="church-identity">
      <div class="church-identity__dot"></div>
      <div class="church-identity__name">Bright Harbor Community Church</div>
    </section>

    <section class="event-logo">
      <span class="event-logo__free">FREE</span>
      <h1 class="event-logo__name" style="margin:0;font-weight:400;">
        <span class="event-logo__name-top">Tots</span>
        <span class="event-logo__name-bottom">Jamboree</span>
      </h1>
      <p class="event-logo__details" style="margin-bottom:0;">
        Sept 19, 2020<br>
        10am - 2pm
      </p>
    </section>
  </main>
</body>
</html>
```